Letterhead Design Project

Letterhead for a Consultant Cardiologist in Adelaide Australia. Should be very classy, mature and imposing. I would prefer colours that portray confidence, gentleness and serenity.

The PDF attached is for you to see the details that will be on the letterhead and not the design which is extremely poor!

Target Market(s)

Health professionals especially medical doctors

Industry/Entity Type

Consultant

```html
<!DOCTYPE html>
<html lang="en">
<head>
<meta charset="utf-8">
<title>Letterhead – Dr Kelechi. A. Morven, Cardiologist</title>
<link rel="stylesheet" href="https://fonts.googleapis.com/css2?family=Cabin:wght@400;500&family=Ubuntu:ital,wght@0,500;0,700;1,700&display=swap">
<style>
  :root {
    --red: #c4161c;
    --red-dark: #a8151a;
    --grey-band: #8f9296;
    --grey-light: #e9eaeb;
    --grey-mid: #c9cbcd;
    --ink: #1e1e1e;
    --ink-soft: #7b7b7b;
    --paper: #ffffff;
  }
  html, body { margin: 0; padding: 0; overflow: hidden; background: var(--paper); }
  .letterhead {
    position: relative;
    width: 848px; height: 1200px;
    overflow: hidden;
    background: var(--paper);
    font-family: "Cabin", sans-serif;
  }
  .header-backdrop {
    position: absolute; left: 0; top: 0; width: 848px; height: 158px;
    background: linear-gradient(90deg, var(--grey-light) 0%, #f3f3f3 35%, var(--grey-mid) 70%, #b9bbbd 100%);
  }
  .header-rule { position: absolute; left: 0; top: 0; }
  .brand-dot {
    position: absolute; left: 42px; top: 52px;
    width: 62px; height: 62px; border-radius: 50%;
    background: var(--red);
  }
  .doctor-name {
    position: absolute; left: 168px; top: 50px; margin: 0;
    font-family: "Ubuntu", sans-serif; font-weight: 700;
    font-size: 19px; color: var(--ink); letter-spacing: 0.2px;
  }
  .credentials {
    position: absolute; left: 169px; top: 85px; margin: 0;
    font-family: "Ubuntu", sans-serif; font-weight: 500;
    font-size: 12px; color: #3c3c3c; letter-spacing: 1px;
  }
  .specialty {
    position: absolute; left: 169px; top: 102px; margin: 0;
    font-family: "Ubuntu", sans-serif; font-weight: 700; font-style: italic;
    font-size: 15px; color: var(--red-dark);
  }
  .footer-block {
    position: absolute; top: 1071px; margin: 0;
    font-size: 12.5px; line-height: 15.6px; color: var(--ink-soft);
    font-style: normal;
  }
  .footer-block .title { color: var(--red-dark); font-size: 13px; }
  .footer-block .dark { color: var(--ink); }
  .footer-consulting { left: 28px; }
  .footer-northbank { left: 209px; }
  .footer-bayview { left: 567px; }
  .gap { display: inline-block; width: 22px; }
  .footer-bands { position: absolute; left: 0; top: 1160px; }
</style>
</head>
<body>
<div class="letterhead">
  <div class="header-backdrop" role="img" aria-label="Soft grey header panel with a faint repeating heart pattern"></div>
  <svg class="header-rule" width="848" height="190" viewBox="0 0 848 190" aria-hidden="true">
    <rect x="0" y="157" width="848" height="4" fill="var(--grey-band)"/>
    <rect x="0" y="161" width="848" height="5" fill="var(--red)"/>
    <polygon points="648,166 848,166 848,186 668,186" fill="var(--grey-band)"/>
  </svg>

  <div class="brand-dot" aria-hidden="true"></div>
  <h1 class="doctor-name">Dr Kelechi. A. Morven</h1>
  <p class="credentials">M.B.B.S, F.M.C.P, F.R.A.C.P</p>
  <p class="specialty">Cardiologist</p>

  <address class="footer-block footer-consulting">
    <span class="title">Consulting</span><br>
    <span class="title">The Riverside Specialist Centre</span><br>
    48 Lantana Road<br>
    Harlow South SA 5090<br>
    <span class="dark">T: 8355 6201</span><br>
    <span class="dark">F: 8366 4412</span>
  </address>

  <address class="footer-block footer-northbank">
    <span class="title">Provider No: 512840QT</span><br>
    <span class="title">Northbank Cardiology</span><br>
    &amp; Specialist Clinic, Marlowe District, Private Hospital<br>
    12-18 Fenwick Road, Ashgrove Vale SA 5120<br>
    <span class="dark">T: 8377 1820<span class="gap"></span>F: 8377 1821</span><br>
    E: cardiology@nbcs.com.au<span class="gap"></span><span class="dark">Provider No: 512840QR</span>
  </address>

  <address class="footer-block footer-bayview">
    <span class="title">Bayview Regional Hospital</span><br>
    26 Harbour Road<br>
    Bayview 5710<br>
    <span class="dark">T: 8690 3300</span><br>
    <span class="dark">F: 8366 4412</span><br>
    <span class="dark">Provider No: 512840QS</span>
  </address>

  <svg class="footer-bands" width="848" height="40" viewBox="0 0 848 40" aria-hidden="true">
    <polygon points="0,6 706,6 724,24 0,24" fill="var(--grey-mid)"/>
    <rect x="0" y="24" width="848" height="16" fill="var(--red)"/>
  </svg>
</div>
</body>
</html>
```